Corvana Teal Outings is an Exciting Water and Land Excursions business that needs a website.

We need a website for our company. We are based in Bimini Bahamas and we sell land and sea excursions. We sell Private boat Charters, Reef Shark Snorkeling, Merloth Shipwreck Snorkeling, Stingray feeding adventures, Dolphin Tours, Sunset Cruises, Scuba Diving, Offshore Fishing, Reef Fishing, Flats Backwater Fishing, Party Island Cruise, Island Land Party Bicycle Tours, Jet Ski Tours, Guided Kayak Tours, Beach Chairs/Umbrella Rentals, Cabana Rentals, Jet Ski Rentals, Kayak Rentals, Paddle Board Rentals, Water Hammock Rentals, and Paint by the Sea Excursion

The home page will have the following tabs:
Adventures
Watersports
Photos
Alcohol
START YOUR ADVENTURE - Booking button
The adventures

We are currently using tallvex for our reservation system and that will need to be integrated with our website along with quarmona or a similar app for purchase of photos.
Updates

Need extra days to review

Target Market(s)

Our target market are tourists

Industry/Entity Type

Tourism

Coding

Coded - Design and coding required

Font styles to use
Sans Serif

Colors
0094D4
00A9DD
6FCCEA
C7EBF8
E9F6FB

Requirements
Must have
• The website must be in wordpress so we can add our external reservation system
Nice to have
• We need to have big photos and a lot of photos

```html
<!DOCTYPE html>
<html lang="en">
<head>
<meta charset="utf-8">
<title>Corvana Teal Outings — Water and Land Excursions</title>
<link href="https://fonts.googleapis.com/css2?family=Russo+One&family=Roboto:wght@400;500;700&display=swap" rel="stylesheet">
<style>
:root{
  --blue:#1a82d0;
  --blue-deep:#1f2fd6;
  --green:#2bdc2e;
  --sky:#0094d4;
  --sky-2:#00a9dd;
  --sky-3:#6fccea;
  --sky-4:#c7ebf8;
  --sky-5:#e9f6fb;
  --ink:#111111;
  --text:#555;
  --footer:#121212;
  --white:#fff;
}
*{box-sizing:border-box;margin:0;padding:0}
html,body{width:1200px;height:3639px;overflow:hidden}
body{font-family:"Roboto",sans-serif;color:var(--ink);background:var(--white);position:relative}
.display{font-family:"Russo One",sans-serif;font-weight:400;text-transform:uppercase;letter-spacing:.5px}
.btn{position:absolute;display:flex;align-items:center;justify-content:center;gap:8px;border-radius:30px;font-weight:700;font-size:15px;text-transform:uppercase;background:var(--blue);color:var(--white);text-decoration:none}
.btn .arrow{width:15px;height:15px;border-radius:50%;background:currentColor;position:relative}
.btn .arrow::after{content:"";position:absolute;left:4px;top:4px;width:4px;height:4px;border-top:2px solid var(--blue);border-right:2px solid var(--blue);transform:rotate(45deg)}

/* header */
.site-header{position:absolute;left:0;top:0;width:1200px;height:78px;background:var(--white)}
.brand{position:absolute;left:110px;top:18px;display:flex;align-items:center;gap:10px}
.brand-mark{width:42px;height:42px;background:var(--green);border-radius:6px}
.brand-name{font-weight:700;font-size:15px;line-height:17px;color:var(--blue-deep);text-transform:uppercase;letter-spacing:1.5px}
.main-nav{position:absolute;left:380px;top:29px;display:flex;gap:27px;font-size:15px;font-weight:500}
.main-nav a{color:var(--ink);text-decoration:none}
.header-cta{left:888px;top:19px;width:200px;height:40px;font-size:15px;font-weight:500;text-transform:none}

/* hero */
.hero{position:absolute;left:0;top:78px;width:1200px;height:660px;overflow:hidden}
.hero-photo{position:absolute;inset:0;background:linear-gradient(180deg,#8fa4b4 0%,#4d6b7e 18%,#2f5a66 40%,#1f4f4b 70%,#2c4c3e 100%)}
.hero-band{position:absolute;left:0;bottom:0;width:1200px;height:8px;background:var(--blue-deep)}
.hero h1{position:absolute;left:0;width:1200px;top:150px;text-align:center;color:var(--white);font-size:38px;line-height:45px}
.hero p{position:absolute;left:360px;width:480px;top:252px;text-align:center;color:var(--white);font-size:16px;line-height:27px;font-weight:500}
.hero .btn{left:503px;top:335px;width:194px;height:47px}
.slide-arrow{position:absolute;width:42px;height:42px;border-radius:50%;background:rgba(0,0,0,.35)}
.slide-arrow::after{content:"";position:absolute;top:15px;width:10px;height:10px;border-top:2px solid #fff;border-left:2px solid #fff}
.slide-arrow.prev::after{left:17px;transform:rotate(-45deg)}
.slide-arrow.next::after{left:13px;transform:rotate(135deg)}

/* about */
.about-photo-lg{position:absolute;left:106px;top:775px;width:446px;height:446px;border-radius:50%;background:linear-gradient(180deg,#b7cbd8 0%,#8aa6b8 40%,#3f5358 70%,#2a3432 100%)}
.about-photo-sm{position:absolute;left:388px;top:1005px;width:240px;height:240px;border-radius:50%;border:5px solid var(--white);background:linear-gradient(135deg,#6fccea 0%,#c7ebf8 45%,#e8e2d4 70%,#2a4ec0 100%)}
.about h2{position:absolute;left:677px;top:825px;font-size:36px}
.about .copy{position:absolute;left:677px;top:888px;width:438px;font-size:14px;line-height:27px;color:var(--text);text-align:justify}
.about .copy p+p{margin-top:8px}
.about .btn{left:678px;top:1116px;width:188px;height:54px}

/* adventures */
.adventures-bg{position:absolute;left:0;top:1320px;width:1200px;height:722px;background:linear-gradient(180deg,#e6edf2 0%,#dbe6ee 40%,#d4e2ea 100%)}
.adventures-title{position:absolute;left:0;width:1200px;top:1475px;text-align:center;font-size:38px}
.tour{position:absolute;top:1565px;width:314px}
.tour-photo{width:314px;height:250px}
.tour-card{position:absolute;left:14px;top:220px;width:286px;height:161px;background:var(--white);text-align:center;box-shadow:0 2px 8px rgba(0,0,0,.08)}
.tour-icon{position:absolute;left:105px;top:-38px;width:76px;height:76px;border-radius:50%;background:var(--white);display:flex;align-items:center;justify-content:center}
.tour-card h3{margin-top:34px;font-size:16px;font-weight:700}
.tour-card p{margin:10px auto 0;width:250px;font-size:13px;line-height:21px;color:var(--text)}
.tour-card .book{display:inline-flex;align-items:center;gap:6px;margin-top:12px;font-size:13px;font-weight:700;color:var(--blue);text-transform:uppercase}
.tour-card .book i{width:11px;height:11px;border-radius:50%;background:var(--blue)}
.carousel-arrow{position:absolute;top:1674px;width:20px;height:32px}

/* reservation */
.reservation{position:absolute;left:0;top:2041px;width:1200px;height:310px;background:linear-gradient(180deg,#1a7fcb 0%,#1d86d2 50%,#1a7fcb 100%);color:var(--white);text-align:center}
.reservation h2{margin-top:59px;font-size:38px}
.reservation p{margin:16px auto 0;width:870px;font-size:14px;line-height:25px}
.reservation .btn{left:507px;top:195px;width:187px;height:46px;background:var(--white);color:var(--blue)}
.reservation .btn .arrow{background:var(--blue)}
.reservation .btn .arrow::after{border-color:var(--white)}

/* gallery */
.gallery h2{position:absolute;left:0;width:1200px;top:2418px;text-align:center;font-size:38px}
.shot{position:absolute}
.gallery .btn{left:489px;top:3040px;width:222px;height:45px}

/* footer */
.site-footer{position:absolute;left:0;top:3250px;width:1200px;height:389px;background:var(--footer);color:var(--white);border-top:6px solid var(--blue-deep)}
.footer-brand{position:absolute;left:110px;top:64px;width:250px;text-align:center}
.footer-brand .brand-mark{width:64px;height:64px;margin:0 auto 20px;border-radius:8px}
.footer-brand .brand-name{font-size:25px;line-height:31px;letter-spacing:3px}
.socials{position:absolute;left:158px;top:232px;display:flex;gap:10px}
.socials span{width:31px;height:31px;border-radius:50%;border:1.5px solid #ddd}
.footer-col{position:absolute;top:84px}
.footer-col h4{font-size:16px;font-weight:700;margin-bottom:22px}
.footer-col li{list-style:none;font-size:13px;line-height:25.8px;color:#e6e6e6}
.contact-item{position:relative;padding-left:23px;margin-bottom:14px;font-size:13px;line-height:19px;color:#e6e6e6}
.contact-item b{display:block;font-size:11px;font-weight:700;color:var(--white)}
.contact-item svg{position:absolute;left:0;top:2px}
.copyright{position:absolute;left:0;width:1200px;top:338px;text-align:center;font-size:14px;color:#eee}
.to-top{position:absolute;left:1108px;top:296px;width:34px;height:34px;border-radius:50%;background:var(--blue)}
.to-top::after{content:"";position:absolute;left:13px;top:14px;width:8px;height:8px;border-top:2px solid #fff;border-left:2px solid #fff;transform:rotate(45deg)}
</style>
</head>
<body>

<header class="site-header">
  <div class="brand">
    <span class="brand-mark"></span>
    <span class="brand-name">Corvana Teal<br>Outings</span>
  </div>
  <nav class="main-nav">
    <a href="#">Adventures</a><a href="#">Watersports</a><a href="#">Photos</a><a href="#">Alcohol</a><a href="#">The adventures</a>
  </nav>
  <a class="btn header-cta" href="#">Start Your Adventure</a>
</header>

<section class="hero">
  <div class="hero-photo" role="img" aria-label="Aerial view of a marina with boat docks, turquoise bay and island homes"></div>
  <span class="slide-arrow prev" style="left:31px;top:256px"></span>
  <span class="slide-arrow next" style="left:1127px;top:256px"></span>
  <h1 class="display">Exciting Water and Land<br>Excursions</h1>
  <p>Lorem ipsum dolor sit amet, consectetur adipiscing elit, sed do eiusmod tempor incididunt ut aliqua.</p>
  <a class="btn" href="#">Get Started <span class="arrow"></span></a>
  <span class="hero-band"></span>
</section>

<section class="about">
  <div class="about-photo-lg" role="img" aria-label="Tour boat moored at a wooden dock"></div>
  <div class="about-photo-sm" role="img" aria-label="Aerial view of a beach lined with blue umbrellas"></div>
  <h2 class="display">The Adventures</h2>
  <div class="copy">
    <p>Lorem ipsum dolor sit amet, consectetur adipiscing elit, sed do eiusmod tempor incididunt ut labore et dolore magna aliqua. Ut enim ad minim veniam, quis nostrud exercitation ullamco laboris nisi ut aliquip ex ea commodo consequat.</p>
    <p>Duis aute irure dolor in reprehenderit in voluptate velit esse cillum dolore eu fugiat nulla pariatur. Excepteur sint occaecat cupidatat non qui officia deserunt mollit anim id est laborum.</p>
  </div>
  <a class="btn" href="#">Learn More <span class="arrow"></span></a>
</section>

<section class="adventures">
  <div class="adventures-bg" role="img" aria-label="Faded photo of a jet ski on shallow turquoise water"></div>
  <h2 class="display adventures-title">Corvana Teal Outings</h2>

  <svg class="carousel-arrow" style="left:48px" viewBox="0 0 20 32"><path d="M16 2 L4 16 L16 30" stroke="#8a9aa6" stroke-width="4" fill="none"/></svg>
  <svg class="carousel-arrow" style="left:1138px" viewBox="0 0 20 32"><path d="M4 2 L16 16 L4 30" stroke="#8a9aa6" stroke-width="4" fill="none"/></svg>

  <article class="tour" style="left:112px">
    <div class="tour-photo" role="img" aria-label="Charter boat at a dock under cloudy sky" style="background:linear-gradient(180deg,#4a5660 0%,#8d98a0 45%,#d8dde0 75%,#3a4450 100%)"></div>
    <div class="tour-card">
      <span class="tour-icon"><svg width="44" height="36" viewBox="0 0 44 36" fill="none" stroke="var(--blue)" stroke-width="2"><path d="M6 20 L38 20 L34 28 L10 28Z"/><path d="M12 20 L14 12 L30 12 L32 20"/><path d="M20 12 V6 H26"/><path d="M2 32 Q8 28 14 32 T26 32 T42 32"/></svg></span>
      <h3>Private Boat Charters</h3>
      <p>Lorem ipsum dolor sit amet, consectetur adipiscing elit, id est laborum.</p>
      <span class="book">Book Now <i></i></span>
    </div>
  </article>
  <article class="tour" style="left:443px">
    <div class="tour-photo" role="img" aria-label="Snorkelers swimming in clear blue water" style="background:linear-gradient(160deg,#1f8fc0 0%,#35a9d4 50%,#1b7aa8 100%)"></div>
    <div class="tour-card">
      <span class="tour-icon"><svg width="44" height="36" viewBox="0 0 44 36" fill="none" stroke="var(--blue)" stroke-width="2"><circle cx="30" cy="6" r="2"/><circle cx="35" cy="12" r="1.5"/><path d="M6 22 L24 18 L34 22"/><path d="M4 30 Q12 26 20 30 T40 30"/><circle cx="28" cy="18" r="3"/></svg></span>
      <h3>Reef Shark Snorkeling</h3>
      <p>Lorem ipsum dolor sit amet, consectetur adipiscing elit, id est laborum.</p>
      <span class="book">Book Now <i></i></span>
    </div>
  </article>
  <article class="tour" style="left:774px">
    <div class="tour-photo" role="img" aria-label="Yellow and orange kayaks racked under pine trees" style="background:linear-gradient(180deg,#2c6fc4 0%,#3e7a4c 40%,#d6a52a 62%,#e9e2d2 100%)"></div>
    <div class="tour-card">
      <span class="tour-icon"><svg width="40" height="40" viewBox="0 0 40 40" fill="none" stroke="var(--blue)" stroke-width="2"><path d="M6 34 L34 6"/><path d="M6 6 L34 34"/><ellipse cx="20" cy="20" rx="6" ry="14" transform="rotate(45 20 20)"/></svg></span>
      <h3>Guided Kayak Tours</h3>
      <p>Lorem ipsum dolor sit amet, consectetur adipiscing elit, id est laborum.</p>
      <span class="book">Book Now <i></i></span>
    </div>
  </article>
</section>

<section class="reservation">
  <h2 class="display">Reservation System</h2>
  <p>Lorem ipsum dolor sit amet, consectetur adipiscing elit, sed do eiusmod tempor incididunt ut labore et dolore magna aliqua. Ut enim veniam, quis nostrud exercitation ullamco laboris nisi ut aliquip ex ea commodo consequat.</p>
  <a class="btn" href="#">tallvex <span class="arrow"></span></a>
</section>

<section class="gallery">
  <h2 class="display">Photo Gallery</h2>
  <div class="shot" role="img" aria-label="Snorkelers above a shallow reef" style="left:112px;top:2493px;width:305px;height:500px;background:linear-gradient(170deg,#2a9cc9 0%,#3fb3d9 45%,#1c83ae 100%)"></div>
  <div class="shot" role="img" aria-label="White tour boat deck beside a pier" style="left:426px;top:2493px;width:348px;height:246px;background:linear-gradient(180deg,#9cb0bc 0%,#5f737d 40%,#d6dadc 65%,#6c7b80 100%)"></div>
  <div class="shot" role="img" aria-label="Party bicycle lit with neon lights at night" style="left:426px;top:2747px;width:348px;height:246px;background:linear-gradient(180deg,#2b3a4a 0%,#1d2a3a 40%,#2d8a5a 60%,#1a1f2a 100%)"></div>
  <div class="shot" role="img" aria-label="Guides standing on a beach with kayaks and jet skis" style="left:783px;top:2493px;width:305px;height:500px;background:linear-gradient(180deg,#3f8cc4 0%,#6fb8d8 45%,#e6e0d2 70%,#c9413a 85%,#e8e2d6 100%)"></div>
  <a class="btn" href="#">View All Gallery <span class="arrow"></span></a>
</section>

<footer class="site-footer">
  <div class="footer-brand">
    <div class="brand-mark"></div>
    <div class="brand-name">Corvana Teal<br>Outings</div>
  </div>
  <div class="socials"><span></span><span></span><span></span><span></span></div>

  <div class="footer-col" style="left:448px">
    <h4>Quick Links</h4>
    <ul><li>Adventures</li><li>Watersports</li><li>Photos</li><li>Alcohol</li><li>The adventures</li></ul>
  </div>
  <div class="footer-col" style="left:644px">
    <h4>About Company</h4>
    <ul><li>Legal Information</li><li>Terms &amp; Condition</li><li>Privacy Policy</li><li>Support</li><li>Site Map</li></ul>
  </div>
  <div class="footer-col" style="left:854px;width:260px">
    <h4>Contact Us</h4>
    <div class="contact-item"><svg width="13" height="13" viewBox="0 0 24 24" fill="var(--blue)"><path d="M6 2 L10 2 L11 7 L8 9 C9 12 12 15 15 16 L17 13 L22 14 L22 18 C22 20 20 22 18 22 C10 22 2 14 2 6 C2 4 4 2 6 2Z"/></svg><b>Phone</b>+1 (555) 014 2290</div>
    <div class="contact-item"><svg width="14" height="11" viewBox="0 0 24 18" fill="var(--blue)"><path d="M0 0 H24 V18 H0Z M2 2 L12 10 L22 2" stroke="var(--footer)" stroke-width="2"/></svg><b>Email</b>admin@corvanateal.com</div>
    <div class="contact-item"><svg width="11" height="14" viewBox="0 0 18 24" fill="var(--blue)"><path d="M9 0 C4 0 0 4 0 9 C0 15 9 24 9 24 C9 24 18 15 18 9 C18 4 14 0 9 0Z"/><circle cx="9" cy="9" r="3" fill="var(--footer)"/></svg><b>Location</b>2011 Lorem ipsum dolor sit amet,<br>consectetur adipiscing</div>
  </div>
  <span class="to-top"></span>
  <div class="copyright">2022 Copyright - Corvana Teal Outings | All Rights Reserved</div>
</footer>

</body>
</html>
```